Software Application page - product section

I have developed a proposal generation application and want to improve the main user interface page.
This is the most important and most used page within my application and therefore it needs to look slick, clean, simple and easy to understand whilst looking very professional, creditable and established.
This is the page in which the user makes certain selections of products and the system will in turn display information on the product selected. The user can then add the product to the basket and the system also calculates the monthly cost of the product along with the profit the user makes by offering the particular product.
I have put something together myself and uploaded accordingly to give you an idea as to what it currently looks like and the structure that it needs to follow.
Section 1
This displays the Customer's account, proposal ID, Customer name etc
Section 2
I have these as radio buttons that the user selects, then clicks on the 'Search product' button. The items will then be displayed in section 3
Section 3
This datagrid displays the available products based on the section 2's selections
Section 4
shows information on the product that has been highlighed in section 3's datagrid. The user then clicks in qty field to enter the qty and then clicks the ADD shopping basket button to add the product to the basket in section 5 datagrid.
Section 5
This is the datagrid/shopping basket that displays all the products that the user has added.
Section 6
Displays all the figures including the total qtys', costs, revenue etc
WHILST IT IS IMPORTANT THAT THE DESIGN MUST FOLLOW THE STRUCTURE OF WHAT IS ATTACHED. I MUST POINT OUT THAT I AM NOT HAPPY WITH THE CURRENT DESIGN. I DO NOT LIKE THE LOOK AND FEEL OF THE CURRENT DESIGN AS IT LOOKS CHEAP AND AMATEURISH.
THE RADIO BUTTONS IN SECTION 1 FOR EXAMPLE SHOULD BE MORE CREATIVE, THE SIZE OF EACH SECTIONS CURRENTLY LOOK DISPROPORTIONATE. THE COLOURS ARE ALL OVER THE PLACE.
THE SIZE OF PAGE MUST BE 1009 X 689
PLEASE VISIT OUT OUR WEBSITE TO STICK TO THE COMPANIES BRAND: www.velmodane.co.uk
I have other pages within my application that require designs along with icons and a lot of work on the website also require redesigning so the best design will also be given this work
Many thanks
Gareth
Software

```html
<!DOCTYPE html>
<html lang="en">
<head>
<meta charset="utf-8">
<title>Velmodane – Proposal Products</title>
<link href="https://fonts.googleapis.com/css2?family=Arimo:wght@400;700&display=swap" rel="stylesheet">
<style>
:root{
  --bg:#e9c9ee;
  --page:#fafafa;
  --purple:#7f5587;
  --purple-line:#94709b;
  --panel:#f2f2f2;
  --panel-border:#e2e2e2;
  --field:#ffffff;
  --field-border:#dcdcdc;
  --text:#333333;
  --row-line:#e4e4e4;
  --search:#e4e4e4;
  --scroll:#dadada;
  --scroll-track:#ffffff;
  --grey-btn:#727272;
  --fixed-row:#f9e3f6;
  --other-row:#cf8fd9;
}
*{box-sizing:border-box;margin:0;padding:0}
html,body{width:1200px;height:1092px;overflow:hidden;background:var(--bg);font-family:"Arimo",Arial,sans-serif;color:var(--text)}
.stage{position:absolute;left:0;top:0;width:1120px;height:1018px;transform:scale(1.0714);transform-origin:0 0}
.abs{position:absolute}
.page{left:55px;top:53px;width:1009px;height:909px;background:var(--page);box-shadow:0 1px 4px rgba(0,0,0,.12)}
.nav{left:55px;top:53px;width:1009px;height:52px;background:var(--purple);display:flex}
.brand{width:179px;height:52px;background:#ececec;display:flex;align-items:center;gap:8px;padding-left:12px;font-size:28px;color:var(--purple);letter-spacing:-.5px}
.brand-dot{width:30px;height:30px;border-radius:50%;background:var(--purple)}
.nav-item{color:#fff;font-size:16px;display:flex;align-items:center;justify-content:center;border-right:1px solid var(--purple-line)}
.panel{background:var(--panel);border:1px solid var(--panel-border)}
.info{left:75px;top:124px;width:465px;height:78px;font-size:14px}
.info span{position:absolute}
.lbl{color:var(--purple)}
.filters{left:75px;top:222px;width:465px;height:271px}
.frow{position:absolute;left:18px;right:18px;height:1px;background:#e0e0e0}
.radio{position:absolute;display:flex;align-items:center;gap:8px;font-size:14px;transform:translateY(-50%)}
.radio i{width:16px;height:16px;border-radius:50%;border:1px solid #8d7393;background:#fff;position:relative}
.radio.on i::after{content:"";position:absolute;left:3px;top:3px;width:8px;height:8px;border-radius:50%;background:var(--purple)}
.search{left:75px;top:448px;width:465px;height:45px;background:var(--search);font-size:14px;padding:14px 0 0 23px}
.search-btn{left:488px;top:448px;width:52px;height:45px;background:var(--purple);display:flex;align-items:center;justify-content:center}
.grid-head{background:var(--purple);color:#fff;font-size:14px}
.cell{position:absolute;font-size:14px;transform:translateY(-50%)}
.vline{position:absolute;width:1px;background:#d6d6d6}
.hline{position:absolute;height:1px;background:var(--row-line)}
.scroll-track{background:var(--scroll-track);border:1px solid #e4e4e4}
.thumb{background:var(--scroll)}
.arrow-sm{position:absolute;width:0;height:0}
.field{background:var(--field);border:1px solid var(--field-border);font-size:14px;padding:11px 10px}
.btn{background:var(--purple);display:flex;align-items:center;justify-content:center;color:#fff;box-shadow:0 2px 0 #5d3c64}
.btn.grey{background:var(--grey-btn);box-shadow:0 2px 0 #4e4e4e}
.delete{font-weight:700;font-size:14px}
.sum-head{font-weight:700;font-size:14px;text-align:center;line-height:16px}
.bold{font-weight:700}
</style>
</head>
<body>
<div class="stage">
  <div class="abs page"></div>

  <nav class="abs nav">
    <div class="brand"><span class="brand-dot"></span>Velmodane</div>
    <div class="nav-item" style="width:104px">Home</div>
    <div class="nav-item" style="width:86px">Task</div>
    <div class="nav-item" style="width:113px">Reports</div>
    <div class="nav-item" style="width:113px">Contact</div>
    <div class="nav-item" style="width:105px">Setting</div>
  </nav>

  <!-- Proposal details -->
  <section class="abs panel info">
    <span class="lbl" style="left:23px;top:13px">Proposal Id&nbsp; :</span><span style="left:117px;top:13px">1334235</span>
    <span class="lbl" style="left:231px;top:13px">Customer Id</span><span style="left:345px;top:13px">:&nbsp; 110399</span>
    <span style="left:23px;top:43px">Status</span><span style="left:104px;top:43px">:&nbsp; Incomplete</span>
    <span class="lbl" style="left:231px;top:43px">Customer Name</span><span style="left:345px;top:43px">:&nbsp; Velmodane Ltd</span>
  </section>

  <!-- Product filters -->
  <section class="abs panel filters">
    <label class="radio on" style="left:21px;top:25px"><i></i>Mobile</label>
    <label class="radio" style="left:171px;top:25px"><i></i>Fixed Line</label>
    <label class="radio" style="left:308px;top:25px"><i></i>Other Products</label>
    <div class="frow" style="top:47px"></div>
    <label class="radio on" style="left:21px;top:70px"><i></i>Aerolink</label>
    <label class="radio" style="left:105px;top:70px"><i></i>Vantafon</label>
    <label class="radio" style="left:224px;top:70px"><i></i>Eastel</label>
    <label class="radio" style="left:308px;top:70px"><i></i>Amberline</label>
    <div class="frow" style="top:93px"></div>
    <label class="radio" style="left:21px;top:116px"><i></i>New</label>
    <label class="radio" style="left:171px;top:116px"><i></i>Resign</label>
    <div class="frow" style="top:138px"></div>
    <label class="radio" style="left:21px;top:160px"><i></i>12</label>
    <label class="radio" style="left:90px;top:160px"><i></i>24</label>
    <label class="radio" style="left:159px;top:160px"><i></i>36</label>
    <label class="radio" style="left:232px;top:160px"><i></i>48</label>
    <label class="radio" style="left:301px;top:160px"><i></i>60</label>
    <label class="radio" style="left:371px;top:160px"><i></i>Other</label>
    <div class="frow" style="top:181px"></div>
    <label class="radio on" style="left:21px;top:202px"><i></i>Share Plan</label>
    <label class="radio" style="left:145px;top:202px"><i></i>Single Plan</label>
    <label class="radio" style="left:272px;top:202px"><i></i>MBB</label>
    <label class="radio" style="left:359px;top:202px"><i></i>Add-On</label>
  </section>
  <div class="abs search">Search Product...</div>
  <div class="abs search-btn">
    <svg width="24" height="24" viewBox="0 0 24 24" fill="none" stroke="#fff" stroke-width="2.6"><circle cx="10" cy="10" r="7.5"/><line x1="15.5" y1="15.5" x2="22" y2="22" stroke-linecap="round"/></svg>
  </div>

  <!-- Tariff grid -->
  <section class="abs" style="left:75px;top:513px;width:465px;height:355px;background:#f2f2f2;border:1px solid #e2e2e2">
    <div class="abs grid-head" style="left:0;top:0;width:463px;height:44px"></div>
    <span class="cell" style="left:23px;top:22px;color:#fff">TARRIF</span>
    <span class="cell" style="left:354px;top:22px;color:#fff">PRICE</span>
    <div class="vline" style="left:297px;top:0;height:331px;background:#d2d2d2"></div>
    <div class="hline" style="left:0;width:440px;top:76px;background:#fff"></div>
    <div class="hline" style="left:0;width:440px;top:108px;background:#fff"></div>
    <div class="hline" style="left:0;width:440px;top:140px;background:#fff"></div>
    <div class="hline" style="left:0;width:440px;top:172px;background:#fff"></div>
    <div class="hline" style="left:0;width:440px;top:204px;background:#fff"></div>
    <div class="hline" style="left:0;width:440px;top:236px;background:#fff"></div>
    <div class="hline" style="left:0;width:440px;top:268px;background:#fff"></div>
    <div class="hline" style="left:0;width:440px;top:300px;background:#fff"></div>
    <span class="cell" style="left:24px;top:60px">Business Single 300</span><span class="cell" style="left:354px;top:60px">19.03</span>
    <span class="cell" style="left:24px;top:92px">Business Single 600</span><span class="cell" style="left:354px;top:92px">25.03</span>
    <span class="cell" style="left:24px;top:124px">Business Single 900</span><span class="cell" style="left:354px;top:124px">19.03</span>
    <span class="cell" style="left:24px;top:156px">Business Single 1200</span><span class="cell" style="left:354px;top:156px">25.03</span>
    <span class="cell" style="left:24px;top:188px">Business Single 300</span><span class="cell" style="left:354px;top:188px">19.03</span>
    <span class="cell" style="left:24px;top:220px">Business Single 600</span><span class="cell" style="left:354px;top:220px">25.03</span>
    <span class="cell" style="left:24px;top:252px">Business Single 900</span><span class="cell" style="left:354px;top:252px">19.03</span>
    <span class="cell" style="left:24px;top:284px">Business Single 1200</span><span class="cell" style="left:354px;top:284px">25.03</span>
    <span class="cell" style="left:24px;top:316px">Business Single 1200</span><span class="cell" style="left:354px;top:316px">25.03</span>
    <div class="abs scroll-track" style="left:440px;top:44px;width:23px;height:287px"></div>
    <div class="abs thumb" style="left:441px;top:79px;width:22px;height:78px"></div>
    <svg class="abs" style="left:446px;top:49px" width="12" height="8"><polyline points="1,7 6,2 11,7" fill="none" stroke="#c4c4c4"/></svg>
    <svg class="abs" style="left:446px;top:318px" width="12" height="8"><polyline points="1,1 6,6 11,1" fill="none" stroke="#c4c4c4"/></svg>
    <div class="abs scroll-track" style="left:0;top:331px;width:463px;height:22px"></div>
    <div class="abs thumb" style="left:37px;top:332px;width:110px;height:21px"></div>
    <svg class="abs" style="left:6px;top:336px" width="8" height="12"><polyline points="7,1 2,6 7,11" fill="none" stroke="#c4c4c4"/></svg>
    <svg class="abs" style="left:427px;top:336px" width="8" height="12"><polyline points="1,1 6,6 1,11" fill="none" stroke="#c4c4c4"/></svg>
  </section>

  <!-- Selected product details -->
  <section class="abs panel" style="left:580px;top:124px;width:465px;height:223px"></section>
  <div class="abs field" style="left:595px;top:140px;width:175px;height:37px">Product</div>
  <div class="abs field" style="left:782px;top:140px;width:112px;height:37px">Qty</div>
  <div class="abs field" style="left:906px;top:140px;width:124px;height:37px">Total Cost</div>
  <div class="abs field" style="left:595px;top:187px;width:175px;height:37px">Reveneu %</div>
  <div class="abs field" style="left:782px;top:187px;width:112px;height:37px">Minutes</div>
  <div class="abs field" style="left:906px;top:187px;width:124px;height:37px">Texts</div>
  <div class="abs field" style="left:595px;top:233px;width:435px;height:56px">Data</div>
  <div class="abs btn" style="left:758px;top:300px;width:51px;height:35px">
    <svg width="12" height="24" viewBox="0 0 12 24" fill="#fff"><circle cx="6" cy="3.5" r="3"/><rect x="2" y="9" width="7" height="11"/><rect x="1" y="20" width="10" height="3"/><rect x="1" y="9" width="3" height="2.5"/></svg>
  </div>
  <div class="abs btn grey" style="left:817px;top:300px;width:51px;height:35px">
    <svg width="26" height="22" viewBox="0 0 26 22" fill="none" stroke="#fff" stroke-width="2"><path d="M8 9 L13 2 L18 9"/><path d="M2 9 H24 L21 20 H5 Z"/><line x1="9" y1="12" x2="9" y2="17"/><line x1="13" y1="12" x2="13" y2="17"/><line x1="17" y1="12" x2="17" y2="17"/></svg>
  </div>

  <!-- Basket grid -->
  <section class="abs" style="left:580px;top:367px;width:465px;height:164px;background:#f2f2f2;border:1px solid #e2e2e2;overflow:hidden">
    <div class="abs grid-head" style="left:0;top:0;width:463px;height:44px"></div>
    <span class="cell" style="left:23px;top:22px;color:#fff">PRODUCT</span>
    <svg class="abs" style="left:159px;top:17px" width="8" height="10" fill="#fff"><polygon points="4,0 8,4 0,4"/><polygon points="0,6 8,6 4,10"/></svg>
    <span class="cell" style="left:193px;top:22px;color:#fff">TYPE</span>
    <span class="cell" style="left:267px;top:22px;color:#fff">PRICE</span>
    <span class="cell" style="left:349px;top:22px;color:#fff">QTY</span>
    <span class="cell" style="left:407px;top:22px;color:#fff">TOTAL</span>
    <div class="vline" style="left:177px;top:0;height:140px;background:#a888ae"></div>
    <div class="vline" style="left:247px;top:0;height:140px;background:#a888ae"></div>
    <div class="vline" style="left:328px;top:0;height:140px;background:#a888ae"></div>
    <div class="vline" style="left:392px;top:0;height:140px;background:#a888ae"></div>
    <div class="vline" style="left:177px;top:44px;height:96px"></div>
    <div class="vline" style="left:247px;top:44px;height:96px"></div>
    <div class="vline" style="left:328px;top:44px;height:96px"></div>
    <div class="vline" style="left:392px;top:44px;height:96px"></div>
    <div class="hline" style="left:0;width:440px;top:76px;background:#fff"></div>
    <div class="hline" style="left:0;width:440px;top:108px;background:#fff"></div>
    <div class="abs scroll-track" style="left:440px;top:44px;width:23px;height:96px"></div>
    <div class="abs thumb" style="left:441px;top:74px;width:22px;height:24px"></div>
    <svg class="abs" style="left:446px;top:49px" width="12" height="8"><polyline points="1,7 6,2 11,7" fill="none" stroke="#c4c4c4"/></svg>
    <svg class="abs" style="left:446px;top:127px" width="12" height="8"><polyline points="1,1 6,6 11,1" fill="none" stroke="#c4c4c4"/></svg>
    <div class="abs scroll-track" style="left:0;top:140px;width:463px;height:22px"></div>
    <div class="abs thumb" style="left:37px;top:141px;width:110px;height:21px"></div>
    <svg class="abs" style="left:6px;top:145px" width="8" height="12"><polyline points="7,1 2,6 7,11" fill="none" stroke="#c4c4c4"/></svg>
    <svg class="abs" style="left:427px;top:145px" width="8" height="12"><polyline points="1,1 6,6 1,11" fill="none" stroke="#c4c4c4"/></svg>
  </section>
  <div class="abs btn delete" style="left:968px;top:541px;width:76px;height:30px">DELETE</div>

  <!-- Summary -->
  <section class="abs" style="left:580px;top:596px;width:465px;height:271px;background:#f2f2f2">
    <div class="abs grid-head" style="left:0;top:0;width:465px;height:44px"></div>
    <div class="abs sum-head" style="left:200px;top:14px;width:60px;color:#fff">QTY</div>
    <div class="abs sum-head" style="left:273px;top:7px;width:80px;color:#fff">MOTHLY<br>COST</div>
    <div class="abs sum-head" style="left:362px;top:7px;width:90px;color:#fff">MOTHLY<br>REVENUE</div>
    <div class="abs" style="left:0;top:140px;width:465px;height:32px;background:var(--fixed-row)"></div>
    <div class="abs" style="left:0;top:172px;width:465px;height:32px;background:var(--other-row)"></div>
    <div class="abs" style="left:0;top:204px;width:465px;height:67px;background:var(--purple)"></div>

    <span class="cell" style="left:19px;top:60px">Mobile Voice</span>
    <span class="cell" style="left:225px;top:60px">0</span><span class="cell" style="left:309px;top:60px">0</span><span class="cell" style="left:404px;top:60px">0</span>
    <span class="cell" style="left:19px;top:92px">Mobile Data Only</span>
    <span class="cell" style="left:225px;top:92px">0</span><span class="cell" style="left:309px;top:92px">0</span><span class="cell" style="left:404px;top:92px">0</span>
    <span class="cell bold" style="left:19px;top:124px">Mobile Total</span>
    <span class="cell bold" style="left:225px;top:124px">0</span><span class="cell bold" style="left:309px;top:124px">0</span><span class="cell bold" style="left:404px;top:124px">0</span>
    <span class="cell bold" style="left:19px;top:156px">Fixed Line</span>
    <span class="cell bold" style="left:225px;top:156px">-</span><span class="cell bold" style="left:309px;top:156px">0</span><span class="cell bold" style="left:404px;top:156px">0</span>
    <span class="cell bold" style="left:19px;top:188px;color:#fff">Other Products</span>
    <span class="cell bold" style="left:225px;top:188px;color:#fff">-</span><span class="cell bold" style="left:309px;top:188px;color:#fff">0</span><span class="cell bold" style="left:404px;top:188px;color:#fff">0</span>
    <span class="cell bold" style="left:19px;top:225px;color:#fff">Total Monthly Cost</span>
    <span class="cell" style="left:225px;top:225px;color:#fff">-</span><span class="cell bold" style="left:309px;top:225px;color:#fff">0</span><span class="cell" style="left:405px;top:225px;color:#fff">-</span>
    <span class="cell bold" style="left:19px;top:250px;color:#fff">Total Monthly Revenue</span>
    <span class="cell" style="left:225px;top:250px;color:#fff">-</span><span class="cell" style="left:311px;top:250px;color:#fff">-</span><span class="cell bold" style="left:384px;top:250px;color:#fff">999999</span>
  </section>

  <!-- Step navigation -->
  <div class="abs btn" style="left:903px;top:895px;width:66px;height:39px">
    <svg width="32" height="22" viewBox="0 0 32 22" fill="#fff"><polygon points="0,11 13,0 13,7 31,7 31,15 13,15 13,22"/></svg>
  </div>
  <div class="abs btn" style="left:979px;top:895px;width:66px;height:39px">
    <svg width="32" height="22" viewBox="0 0 32 22" fill="#fff"><polygon points="32,11 19,0 19,7 1,7 1,15 19,15 19,22"/></svg>
  </div>
</div>
</body>
</html>
```